Visitenkarte erstellen für Reiki Praxis

Visitenkarten für Reiki Praxis Doppelseitig

business cards reiki practice double-sided

The background can also be a different color

```html
<!DOCTYPE html>
<html lang="en">
<head>
<meta charset="utf-8">
<title>Lumen Balance – Business Cards</title>
<link href="https://fonts.googleapis.com/css2?family=Lato:wght@300;400;700&display=swap" rel="stylesheet">
<style>
  :root {
    --canvas: #e4e4e6;
    --violet: #5a2ca0;
    --charcoal: #383838;
    --white: #ffffff;
    --silver: #c9c9cf;
    --gold: #e0a42a;
    --mauve: #b06a86;
    --grey-text: #a8a8a8;
    --mark-faint: rgba(176, 106, 134, 0.18);
  }
  * { box-sizing: border-box; margin: 0; padding: 0; }
  html, body {
    width: 1200px; height: 900px; overflow: hidden;
    background: var(--canvas);
    font-family: "Lato", sans-serif;
  }
  .sheet {
    width: 1200px; height: 900px;
    display: flex; align-items: center; justify-content: center; gap: 40px;
  }
  .card {
    position: relative;
    width: 540px; height: 309px;
    overflow: hidden;
    box-shadow: 0 12px 30px rgba(0,0,0,0.18);
  }

  /* Front */
  .card-front { background: var(--violet); }
  .front-brand {
    position: absolute; top: 108px; left: 0; right: 0;
    display: flex; align-items: center; justify-content: center; gap: 14px;
  }
  .front-brand .brand-dot {
    width: 34px; height: 34px; border-radius: 50%;
    border: 2px solid var(--silver);
  }
  .front-brand .brand-name {
    font-weight: 300; font-size: 34px; letter-spacing: 3px;
    color: var(--silver); text-transform: uppercase;
  }
  .front-url {
    position: absolute; bottom: 30px; left: 0; right: 0; text-align: center;
    color: var(--white); font-size: 13px; letter-spacing: 5px; font-weight: 400;
  }

  /* Back */
  .card-back { background: var(--charcoal); }
  .back-decor {
    position: absolute; right: -60px; top: -40px;
    width: 300px; height: 300px; border-radius: 50%;
    border: 2px solid var(--mark-faint);
  }
  .back-brand {
    position: absolute; left: 40px; top: 42px;
  }
  .back-brand .brand-row { display: flex; align-items: center; gap: 10px; }
  .back-brand .brand-dot {
    width: 18px; height: 18px; border-radius: 50%;
    border: 1.5px solid var(--gold);
  }
  .back-brand .brand-name {
    color: var(--white); font-size: 24px; font-weight: 400;
    text-transform: uppercase; letter-spacing: 0.5px;
  }
  .practitioner {
    margin-top: 4px; margin-left: 28px;
    color: var(--gold); font-size: 15px; letter-spacing: 4px;
    text-transform: uppercase;
  }
  .contact {
    position: absolute; left: 40px; top: 140px;
    color: var(--white); font-size: 13px; line-height: 1.35;
  }
  .contact address { font-style: normal; margin-bottom: 8px; }
  .contact ul { list-style: none; }
  .contact li { display: flex; align-items: center; gap: 8px; }
  .contact svg { width: 11px; height: 11px; fill: var(--mauve); flex: none; }
  .holder {
    position: absolute; right: 36px; top: 118px; text-align: right;
  }
  .holder-name {
    color: var(--mauve); font-size: 19px; text-transform: uppercase; letter-spacing: 0.5px;
  }
  .holder-title { color: var(--grey-text); font-size: 12px; }
</style>
</head>
<body>
<main class="sheet">

  <section class="card card-front" aria-label="Card front">
    <div class="front-brand">
      <span class="brand-dot"></span>
      <span class="brand-name">Lumen Balance</span>
    </div>
    <p class="front-url">www.LumenBalance.com</p>
  </section>

  <section class="card card-back" aria-label="Card back">
    <span class="back-decor"></span>

    <div class="back-brand">
      <div class="brand-row">
        <span class="brand-dot"></span>
        <span class="brand-name">Lumen Balance</span>
      </div>
      <p class="practitioner">Maren Holt</p>
    </div>

    <div class="contact">
      <address>412 Willow Crest Road<br>Fairbanks, Alaska 99701</address>
      <ul>
        <li><svg viewBox="0 0 12 12"><path d="M2.5 1h2l1 3-1.3 1a6 6 0 0 0 2.8 2.8L8 6.5l3 1v2a1.5 1.5 0 0 1-1.5 1.5A8.5 8.5 0 0 1 1 2.5 1.5 1.5 0 0 1 2.5 1z"/></svg>555-210-4836</li>
        <li><svg viewBox="0 0 12 12"><path d="M3 0h6a1 1 0 0 1 1 1v10a1 1 0 0 1-1 1H3a1 1 0 0 1-1-1V1a1 1 0 0 1 1-1zm0 1.5v8h6v-8z"/></svg>555-318-7702</li>
        <li><svg viewBox="0 0 12 12"><path d="M3 0h6v3H3zM1 4h10v5H9v3H3V9H1zm3 4v3h4V8z"/></svg>555-427-9051</li>
        <li><svg viewBox="0 0 12 12"><path d="M0 2h12v1L6 7 0 3zm0 2.5 6 4 6-4V10H0z"/></svg>hello@LumenBalance.com</li>
        <li><svg viewBox="0 0 12 12"><path d="M6 0a6 6 0 1 0 0 12A6 6 0 0 0 6 0zm0 1.2c.8 1 1.3 2.6 1.4 4.2H4.6C4.7 3.8 5.2 2.2 6 1.2zM4.6 6.6h2.8c-.1 1.6-.6 3.2-1.4 4.2-.8-1-1.3-2.6-1.4-4.2z"/></svg>www.LumenBalance.com</li>
      </ul>
    </div>

    <div class="holder">
      <p class="holder-name">Daniel Reyes</p>
      <p class="holder-title">President</p>
    </div>
  </section>

</main>
</body>
</html>
```